Quolvex custom business card design

Need a authentic, innovative business card design for a new mobile app business. I am uploading a few screen images from our app for you to view. I would like app design theme to match business card design. I can also send logo images.

```html
<!DOCTYPE html>
<html lang="en">
<head>
<meta charset="utf-8">
<title>Quolvex business card</title>
<link rel="stylesheet" href="https://fonts.googleapis.com/css2?family=Montserrat:ital,wght@0,400;0,600;0,700;0,800;0,900;1,300&display=swap">
<style>
  :root {
    --stage: #2a2a2b;
    --purple: #55238a;
    --purple-deep: #2b1642;
    --ink: #111012;
    --panel: #231a1c;
    --paper: #ffffff;
    --mist: #e3e1e5;
    --ghost: #ebe8ee;
    --soft-text: #cfcbd4;
  }
  * { margin: 0; padding: 0; box-sizing: border-box; }
  html, body {
    width: 1200px; height: 1200px; overflow: hidden;
    background: var(--stage);
    font-family: "Montserrat", sans-serif;
  }
  .sheet {
    position: relative; width: 1200px; height: 1200px;
  }
  .card {
    position: absolute; left: 150px; width: 900px; height: 514px;
    overflow: hidden; border-radius: 4px;
    box-shadow: 0 14px 34px rgba(0,0,0,.45);
  }
  .card--front { top: 70px; background: var(--paper); }
  .card--back {
    top: 616px;
    background: linear-gradient(160deg, var(--purple-deep) 0%, #3d1d66 50%, var(--purple) 100%);
  }

  /* front: brand side */
  .brand-area {
    position: absolute; left: 0; top: 0; width: 360px; height: 514px;
    overflow: hidden;
    background: linear-gradient(180deg, var(--mist) 0 56%, var(--paper) 56% 100%);
  }
  .brand-ghost {
    position: absolute; left: 14px; bottom: 24px;
    font-size: 70px; font-weight: 900; color: var(--ghost);
    letter-spacing: -1px; line-height: 1; white-space: nowrap;
  }
  .corner-tab {
    position: absolute; left: 0; top: 0; width: 70px; height: 22px;
    background: var(--purple); border-bottom-right-radius: 14px;
  }
  .brand {
    position: absolute; left: 30px; top: 160px;
    display: flex; align-items: center; gap: 14px;
  }
  .brand-dot {
    width: 64px; height: 64px; border-radius: 50%; background: var(--purple);
    flex: none;
  }
  .brand-name {
    font-size: 42px; font-weight: 900; color: var(--ink); letter-spacing: -1px;
    white-space: nowrap;
  }

  /* front: contact side */
  .contact-area {
    position: absolute; left: 360px; top: 0; width: 540px; height: 514px;
    background: var(--purple);
  }
  .contact-panel {
    position: absolute; left: 0; top: 0; width: 505px; height: 478px;
    background: var(--panel);
    padding: 40px 36px 0 26px;
  }
  .person {
    text-align: right; color: var(--paper);
  }
  .person-name { font-size: 38px; font-weight: 700; letter-spacing: .5px; }
  .person-role {
    font-size: 16px; font-style: italic; font-weight: 300; color: var(--soft-text);
    margin-top: 4px;
  }
  .contact-list {
    list-style: none; margin-top: 46px;
    display: flex; flex-direction: column; gap: 14px;
  }
  .contact-item {
    display: flex; align-items: center; gap: 12px;
    height: 40px; padding: 0 18px 0 4px;
    background: var(--purple); border-radius: 8px;
    color: var(--paper); font-size: 18px; font-weight: 600;
    width: fit-content;
  }
  .contact-icon {
    width: 32px; height: 32px; border-radius: 6px; background: var(--paper);
    display: flex; align-items: center; justify-content: center;
  }
  .contact-icon svg { width: 20px; height: 20px; }

  /* back */
  .seal {
    position: absolute; left: 240px; top: 47px;
    width: 420px; height: 420px; border-radius: 50%;
    background: var(--paper);
    display: flex; align-items: center; justify-content: center; gap: 16px;
  }
  .seal .brand-dot { width: 84px; height: 84px; }
  .seal .brand-name { font-size: 50px; }
</style>
</head>
<body>
<main class="sheet">

  <section class="card card--front" aria-label="Business card front">
    <div class="brand-area">
      <div class="corner-tab"></div>
      <div class="brand-ghost" aria-hidden="true">Quolvex</div>
      <div class="brand">
        <span class="brand-dot"></span>
        <span class="brand-name">Quolvex</span>
      </div>
    </div>

    <div class="contact-area">
      <div class="contact-panel">
        <div class="person">
          <h1 class="person-name">Your Name</h1>
          <p class="person-role">Your Tagline or Position here</p>
        </div>
        <ul class="contact-list">
          <li class="contact-item">
            <span class="contact-icon">
              <svg viewBox="0 0 20 20"><rect x="5" y="2" width="10" height="16" rx="2" fill="none" stroke="#55238a" stroke-width="2"/><circle cx="10" cy="15" r="1" fill="#55238a"/></svg>
            </span>
            +000 12345 875
          </li>
          <li class="contact-item">
            <span class="contact-icon">
              <svg viewBox="0 0 20 20" fill="none" stroke="#55238a" stroke-width="1.6"><circle cx="10" cy="10" r="7.5"/><ellipse cx="10" cy="10" rx="3.2" ry="7.5"/><path d="M2.5 10h15M4 6h12M4 14h12"/></svg>
            </span>
            quolvex.app
          </li>
          <li class="contact-item">
            <span class="contact-icon">
              <svg viewBox="0 0 20 20" fill="none" stroke="#55238a" stroke-width="1.8"><rect x="2" y="4.5" width="16" height="11" rx="1.5"/><path d="M2.5 5.5l7.5 6 7.5-6"/></svg>
            </span>
            hello@quolvexmail.com
          </li>
          <li class="contact-item">
            <span class="contact-icon">
              <svg viewBox="0 0 20 20"><path d="M10 1.8a6 6 0 0 0-6 6c0 4.5 6 10.4 6 10.4s6-5.9 6-10.4a6 6 0 0 0-6-6z" fill="#55238a"/><circle cx="10" cy="7.8" r="2.2" fill="#fff"/></svg>
            </span>
            Street Address, 01 USA
          </li>
        </ul>
      </div>
    </div>
  </section>

  <section class="card card--back" aria-label="Business card back">
    <div class="seal">
      <span class="brand-dot"></span>
      <span class="brand-name">Quolvex</span>
    </div>
  </section>

</main>
</body>
</html>
```